Flyer-Design für Hochzeitswebseiten
Zielgruppe
Wir machen Hochzeitswebseiten ( www.holdtheday-web.de).
Aufgabenstellung
Gerne hätte ich folgendes DIN Format: 210x148 quer mit 6 Seiten. 1 Seite schwarz mit unserem Logo. 2 Seite Bild. 3 Seite Text. 4 Seite 4-5 Bilder. 5 Seite Text. 6 Seite Kontaktinformationen.
Text1:
Ihr habt alles dafür getan, dass Eure Hochzeit so schön wie möglich wird. Wir tun alles dafür, dass die Erinnerung daran so großartig wie möglich bleibt. Ihr stellt uns Eure persönlichen Informationen und Fotos zur Verfügung. Wir machen daraus eine professionelle Website über den schönsten Tag Eures Lebens. Ihr entscheidet über Umfang und Budget.
Wir widmen uns jedem Auftrag mit Begeisterung und Kreativität.
Text2: evtl. sollte da das Basic und Premiumpaket beschrieben werden. Sind uns da aber unsicher.

```html
<!DOCTYPE html>
<html lang="de">
<head>
<meta charset="utf-8">
<title>Hold The Day – Flyer</title>
<link href="https://fonts.googleapis.com/css2?family=Yanone+Kaffeesatz:wght@300;400;500&family=Great+Vibes&display=swap" rel="stylesheet">
<style>
:root{
  --stage:#7d9194;
  --sheet:#ffffff;
  --paper:#f6f5f1;
  --ink:#262626;
  --gold:#c89a1e;
  --gold-light:#e6c45a;
  --black:#050505;
  --white:#ffffff;
}
*{box-sizing:border-box;margin:0;padding:0}
html,body{width:1200px;height:646px;overflow:hidden}
body{background:var(--stage);position:relative;font-family:"Yanone Kaffeesatz",sans-serif;color:var(--ink)}
.strip{position:absolute;left:19px;width:1163px;height:273px;background:var(--sheet)}
.strip--outside{top:39px}
.strip--inside{top:335px}
.panel{position:absolute;top:9px;width:369px;height:255px;overflow:hidden}
.panel--1{left:10px}.panel--2{left:397px}.panel--3{left:785px}

/* pricing */
.pricing{background:var(--paper)}
.package{position:absolute;top:9px;height:237px;border:1.5px solid var(--gold);padding:4px 6px 0 6px;font-size:8.4px;line-height:11px;font-weight:400}
.package--basic{left:7px;width:134px}
.package--premium{left:147px;width:215px}
.package__name{font-family:"Great Vibes",cursive;font-weight:400;color:var(--gold);font-size:25px;line-height:30px;margin-bottom:9px}
.package__price{font-weight:500;font-size:8.4px}
.package__price small{font-size:5px;font-weight:400}
.package__lead{color:var(--gold);font-size:10px;line-height:12px;font-weight:400;margin:3px 0 6px}
.features{list-style:none}
.features li{padding-left:8px;position:relative}
.features li::before{content:"";position:absolute;left:0;top:4px;width:5px;height:2.5px;background:var(--gold);clip-path:polygon(0 50%,60% 0,100% 0,100% 100%,60% 100%)}
.features .gap{margin-top:6px}
.premium-cols{display:flex;gap:6px}
.premium-cols .col-left{width:102px}
.premium-cols .col-right{flex:1}
.extra-lead{color:var(--gold);font-size:10px;line-height:11px;margin:7px 0 8px}

/* contact */
.contact{background:var(--paper)}
.contact__head{position:absolute;top:0;left:0;right:0;height:79px;background:var(--black);display:flex;align-items:center;justify-content:center}
.contact__foot{position:absolute;bottom:0;left:0;right:0;height:55px;background:var(--black);display:flex;align-items:center;padding-left:18px;gap:6px;color:var(--white);font-size:8.5px;font-weight:500}
.contact__invite{position:absolute;top:153px;left:0;right:0;text-align:center;color:var(--gold);font-size:16.5px}
.brand{display:flex;align-items:center;gap:8px;color:var(--gold-light);font-weight:400;letter-spacing:1px}
.brand__dot{border:1.5px solid var(--gold-light);border-radius:50%}
.brand--small{font-size:26px}.brand--small .brand__dot{width:18px;height:18px}
.brand--large{font-size:44px}.brand--large .brand__dot{width:30px;height:30px}
.contact-item{display:flex;align-items:center;gap:4px;margin-right:6px;white-space:nowrap}
.contact-item svg{width:26px;height:26px;flex:none}

.cover{background:var(--black);display:flex;align-items:center;justify-content:center}
.cover .brand{transform:translate(0,-8px)}

/* photos */
.photo{position:absolute}
.photo--beach{left:0;top:0;width:369px;height:254px;background:linear-gradient(180deg,#e4e6e4 0%,#dfe3e2 55%,#bcc7c4 75%,#c8b9a3 100%)}

/* story */
.story{background:var(--black);color:var(--white);font-size:12px;line-height:15.5px}
.story__row{position:absolute;left:0;right:0;display:flex;align-items:center;white-space:nowrap}
.story__cause{width:152px;text-align:right;color:var(--gold)}
.story__arrow{width:40px;display:flex;justify-content:center}
.story__effect{width:175px}
.story__row--1{top:47px}.story__row--2{top:94px}.story__row--3{top:141px}
.story-pointer{position:absolute;left:741px;top:182px}

/* gallery */
.gallery .photo{position:absolute}
.g-flowers{left:0;top:0;width:85px;height:134px;background:linear-gradient(160deg,#9fb3c4,#cfd6d4 55%,#7f9a62)}
.g-bridesmaids{left:93px;top:0;width:132px;height:66px;background:linear-gradient(135deg,#e8e6ea,#d8cbd0 50%,#a7a4c9)}
.g-table{left:93px;top:75px;width:132px;height:63px;background:linear-gradient(135deg,#eef0f4,#c9c3dd 60%,#6f3f7e)}
.g-sunset{left:0;top:147px;width:225px;height:108px;background:linear-gradient(180deg,#bcc9d7 0%,#f0dcc0 45%,#f3c99b 65%,#dcc3ae 100%)}
.g-couple{left:234px;top:0;width:135px;height:254px;background:linear-gradient(120deg,#d9cfc2,#b98f73 50%,#3b2c26)}
</style>
</head>
<body>

<section class="strip strip--outside">
  <article class="panel panel--1 pricing">
    <div class="package package--basic">
      <h2 class="package__name">Basic</h2>
      <p class="package__price">299.– Euro (einmalig) <small>inkl. MwSt</small></p>
      <p class="package__lead">Unser Grundpaket mit</p>
      <ul class="features">
        <li>50GB Speicherplatz</li>
        <li>50 Fotos</li>
        <li>Eine Wunschdomain</li>
        <li>Eigene E-Mailadresse</li>
        <li>Passwortschutz</li>
        <li>SSL Zertifikat</li>
        <li>Keine Werbung</li>
        <li>Optimiert für Smartphones und Tablets</li>
        <li>Keine Verpflichtungen</li>
        <li>Keine automatische Verlängerung</li>
        <li>Eure Webseite als ZIP-Datei</li>
        <li>Hosting &amp; Serverkosten für 1 Jahr</li>
        <li class="gap">Auf Wunsch: Save the Date</li>
      </ul>
    </div>
    <div class="package package--premium">
      <h2 class="package__name">Premium</h2>
      <div class="premium-cols">
        <div class="col-left">
          <p class="package__price">429.– Euro (einmalig) <small>inkl. MwSt</small></p>
          <p class="package__lead">Unser Premiumpaket mit</p>
          <ul class="features">
            <li>Unbegrenzter Speicherplatz</li>
            <li>Unbegrenzte Anzahl an Fotos</li>
            <li>Euer Hochzeitsvideo</li>
            <li>Eine Wunschdomain</li>
            <li>Eigene E-Mailadresse</li>
            <li>Ausführliche Berichte</li>
            <li>Gästebuch</li>
            <li>Verknüpfung mit Euren sozialen Netzwerken</li>
            <li>Passwortschutz</li>
            <li>SSL-Zertifikat</li>
            <li>Keine Werbung</li>
            <li>Optimiert für Smartphones und Tablets</li>
          </ul>
        </div>
        <div class="col-right">
          <ul class="features">
            <li>Keine Verpflichtungen</li>
            <li>Keine automatische Verlängerung</li>
            <li>Eure Webseite als ZIP-Datei</li>
            <li>Hosting &amp; Serverkosten für ein Jahr</li>
            <li class="gap">Auf Wunsch: Save the Date</li>
          </ul>
          <p class="extra-lead">Optional könnt Ihr Eure<br>Webseite erweitern mit:</p>
          <ul class="features">
            <li>Eure Flitterwochen</li>
            <li>Euren Hochzeitstag</li>
            <li>Geburt Eurer Kinder</li>
            <li>Eure Urlaube</li>
            <li>Jubilar</li>
            <li>...etc...</li>
          </ul>
        </div>
      </div>
    </div>
  </article>

  <article class="panel panel--2 contact">
    <header class="contact__head">
      <div class="brand brand--small"><span class="brand__dot"></span>Hold The Day</div>
    </header>
    <p class="contact__invite">Wir freuen uns auf Ihre Kontaktaufnahme!</p>
    <footer class="contact__foot">
      <div class="contact-item">
        <svg viewBox="0 0 26 26"><circle cx="13" cy="13" r="11.5" fill="none" stroke="#e6c45a" stroke-width="1.2"/><path d="M9 7l3 0 1 4-2 1.5c1 2 2 3 3.5 3.5L16 14l4 1v3c-6 1-12-5-11-11z" fill="#e6c45a"/></svg>
        <span>+49 (0) 221 55 01 27 89</span>
      </div>
      <div class="contact-item">
        <svg viewBox="0 0 26 26"><circle cx="13" cy="13" r="11.5" fill="none" stroke="#e6c45a" stroke-width="1.2"/><rect x="6.5" y="8.5" width="13" height="9" fill="#e6c45a"/><path d="M6.5 8.5l6.5 5 6.5-5" fill="none" stroke="#050505" stroke-width="0.9"/></svg>
        <span>info@holdtheday-web.de</span>
      </div>
      <div class="contact-item">
        <svg viewBox="0 0 26 26"><circle cx="13" cy="13" r="11.5" fill="none" stroke="#e6c45a" stroke-width="1.2"/><circle cx="13" cy="13" r="6.5" fill="none" stroke="#e6c45a" stroke-width="1.2"/><ellipse cx="13" cy="13" rx="3" ry="6.5" fill="none" stroke="#e6c45a"/><path d="M6.5 13h13M8 9.5h10M8 16.5h10" stroke="#e6c45a"/></svg>
        <span>www.holdtheday-web.de</span>
      </div>
    </footer>
  </article>

  <article class="panel panel--3 cover">
    <div class="brand brand--large"><span class="brand__dot"></span>Hold The Day</div>
  </article>
</section>

<section class="strip strip--inside">
  <article class="panel panel--1">
    <div class="photo photo--beach" role="img" aria-label="Foto: Bräutigam trägt seine Braut am Strand vor grauem Meer und Himmel"></div>
  </article>

  <article class="panel panel--2 story">
    <div class="story__row story__row--1">
      <p class="story__cause">Ihr habt alles dafür getan, dass Eure<br>Hochzeit so schön wie möglich wird.</p>
      <span class="story__arrow"><svg width="22" height="14" viewBox="0 0 22 14"><path d="M1 12L17 3M17 3l-7 0M17 3l-3 7" fill="none" stroke="#c89a1e" stroke-width="2.2" stroke-linecap="round"/></svg></span>
      <p class="story__effect">Wir tun alles dafür, dass die Erinnerung<br>daran so großartig wie möglich bleibt.</p>
    </div>
    <div class="story__row story__row--2">
      <p class="story__cause">Ihr stellt uns Eure persönlichen<br>Informationen und Fotos zur Verfügung.</p>
      <span class="story__arrow"><svg width="22" height="14" viewBox="0 0 22 14"><path d="M1 12L17 3M17 3l-7 0M17 3l-3 7" fill="none" stroke="#c89a1e" stroke-width="2.2" stroke-linecap="round"/></svg></span>
      <p class="story__effect">Wir machen daraus eine professionelle<br>Website über den schönsten Tag Eures Lebens.</p>
    </div>
    <div class="story__row story__row--3">
      <p class="story__cause">Ihr entscheidet über<br>Umfang und Budget.</p>
      <span class="story__arrow"><svg width="22" height="14" viewBox="0 0 22 14"><path d="M1 12L17 3M17 3l-7 0M17 3l-3 7" fill="none" stroke="#c89a1e" stroke-width="2.2" stroke-linecap="round"/></svg></span>
      <p class="story__effect">Wir widmen uns jedem Auftrag mit<br>Begeisterung und Kreativität.</p>
    </div>
  </article>

  <article class="panel panel--3 gallery">
    <div class="photo g-flowers" role="img" aria-label="Foto: Blumenstrauß in einer Glasvase im Freien"></div>
    <div class="photo g-bridesmaids" role="img" aria-label="Foto: Braut mit Brautjungfern und Sträußen"></div>
    <div class="photo g-table" role="img" aria-label="Foto: festlich gedeckte Hochzeitstafel in Lila"></div>
    <div class="photo g-sunset" role="img" aria-label="Foto: Brautpaar hält sich am Strand bei Sonnenuntergang an den Händen"></div>
    <div class="photo g-couple" role="img" aria-label="Foto: Brautpaar in inniger Umarmung"></div>
  </article>

  <svg class="story-pointer" width="70" height="64" viewBox="0 0 70 64"><path d="M68 1L1 21l21 9L3 52l6 6 19-18 5 21z" fill="#d4a82a" stroke="#f0d77a" stroke-width="1.5" stroke-linejoin="round"/></svg>
</section>

</body>
</html>
```